Zibbles - Inspiring Biscuits - Crunch on this!

We have a current website but have had a complete redesign of our logo and look. We need to bring the site up to scratch with this new look and feel.
Zibble Brief
I have attached the concept document.
• Zibbles – Inspiring Biscuits are the reinvented fortune cookie. Individually wrapped cookies with a motivational message stuck on the outside. They are fun, often cheeky, thought provoking and yum.
• Initially we want to focus on just the adult quote range but will over time add the Zibble kids range. Where we are at at the moment is we have the concept for the Zibble kids but are lining up a graphic artist to design individual pictures for the kids range. We do not own the ones for the kids pics at the moment so are unable to use those specific ones.
• If however you are able to source almost identical ones that we can use for the website without any licensing issues then please feel free to talk to me about this and send some examples.
• We are only at this stage selling in bulk boxes of 60 Zibbles so want a simple shopping cart where we can add to over time. The long term goal is retail.
• I post a quote daily on facebook and have a long winded manual process where I then upload on to linkedin, pinterest, and twitter. I would like to be able to load a quote of the day on to our website and it updates all the rest for me. On FB, Pinterest and Twitter we are Zibblebakes.
• I would also like to be able to use this as a blog – assume it’s the same thing if I am uploading a picture.
• I would like something clean and funky and something we can build on especially when we start going down the path of the kids zibbles as I would in the long term like to get an interactive site for kids to play on and we have all the characters on our Zibbles for the kids to play with.
Based on how we go we may look to crowdfund, so think about this possibility as we will want the website to link in to that if need be.
I am not a control freak and love people whose imagination runs wild. The only restraints I have are the colours that are in the uploaded PDF, the logos used and fonts the designers have selected. The main one used on the quote labels is Avian Bold.
Fonts are :-
apple braille outline 6 dot
avianbol
avianreg
kidsscript - bold
lubalgraboo
lubalingraph - book
I have uploaded what I think you might need to get started, however please feel free to send as many questions you can think of.
Cheers
Fiona
Updates
i have uploaded a load more info and files for the site brief.
Reason: I have had quite a few acceptance and as I am new to this site don't want to upset anyone who has accepted but run out of time.
Thanks to those who have submitted so far we are looking at all of them next week, no one is ruled out at this point. Have to say there are some very talented people out there.
We really appreciate the response and imaginations. Keep you posted
Fiona
Target Market(s)
Anyone that likes motivation. While zibbles are motivational cookies, we are actually in the motivation business not the cookie business.
Industry/Entity Type
Shopping
Requirements
Must have
- Ecommerce - shopping cart
Links to social media twitter, facebook, Pinterest, linkedin the more the merrier.

```html
<!DOCTYPE html>
<html lang="en">
<head>
<meta charset="utf-8">
<title>Zibbles - Inspiring Biscuits - Crunch on this!</title>
<link rel="stylesheet" href="https://fonts.googleapis.com/css2?family=Ubuntu:wght@400;500;700&display=swap">
<style>
:root{
  --navy:#0b356f;
  --navy-dark:#062858;
  --navy-text:#1b3a70;
  --lime:#b6d65c;
  --green:#6c8f1f;
  --frame:#b3c77f;
  --cream:#f8f5ea;
  --logo-bg:#f3efe1;
  --brown:#6a4a33;
  --grey-text:#555555;
  --buy:#c6461d;
  --footer:#2a2a2a;
  --footer-text:#c9c9c9;
  --gold:#e6c23a;
  --pack:#ebe6d6;
  --biscuit:#6b4a36;
}
*{box-sizing:border-box;margin:0;padding:0}
html,body{width:1169px;height:1200px;overflow:hidden}
body{background:var(--cream);font-family:"Ubuntu",sans-serif}
.page{position:relative;width:1150px;height:1180px;transform:scale(1.0165,1.017);transform-origin:0 0;background:var(--cream)}
.abs{position:absolute}
a{color:inherit;text-decoration:none}
h1,h2,h3{font-weight:400}

/* header */
.site-header{left:0;top:0;width:1150px;height:105px;background:linear-gradient(var(--navy),var(--navy-dark))}
.main-nav a{position:absolute;color:#fff;font-size:12.5px;font-weight:500;white-space:nowrap}
.main-nav a::before{content:"»";margin-right:10px;font-size:15px}
.main-nav a.is-current{color:var(--lime)}
.brand{left:399px;top:13px;width:353px;height:160px;z-index:5;background:var(--logo-bg);box-shadow:0 6px 10px rgba(0,0,0,.18);display:flex;align-items:center;justify-content:center;gap:14px}
.brand-name{font-size:58px;font-weight:700;color:var(--navy-text);letter-spacing:1px}
.brand-dot{width:20px;height:20px;border-radius:50%;background:var(--navy-text)}
.cart-title{left:836px;top:19px;color:#fff;font-size:16px;font-weight:700}
.cart-icon{left:848px;top:44px}
.cart-divider{left:907px;top:18px;width:1px;height:66px;background:rgba(255,255,255,.35)}
.cart-info{left:926px;top:20px;color:#fff;font-size:12.5px;line-height:22px}
.cart-info .links{color:var(--lime)}
.cart-info .links span{color:#fff;margin:0 5px}

/* hero */
.hero{left:95px;top:121px;width:960px;height:375px;border:8px solid var(--frame);background:#fff}
.hero-title{left:131px;top:185px;font-size:25px;font-weight:700;color:var(--navy-text)}
.hero-sub{left:131px;top:236px;font-size:16px;color:var(--green)}
.hero-copy{left:131px;top:261px;width:440px;font-size:13px;line-height:26px;letter-spacing:-.2px;color:var(--grey-text)}
.btn-more{left:131px;top:375px;width:91px;height:36px;border-radius:4px;background:linear-gradient(#555,#2e2e2e);color:#fff;font-size:14px;display:flex;align-items:center;justify-content:center}
.slider-dots{left:130px;top:450px;display:flex;gap:9px}
.slider-dots i{width:13px;height:13px;border-radius:50%;background:#8a8a8a}
.slider-dots i:first-child{background:#333}
.hero-box{left:825px;top:143px;width:210px;height:320px;border-radius:14px 14px 4px 4px;background:linear-gradient(100deg,#f4f1e6 0,var(--pack) 60%,#ddd8c6 100%);box-shadow:4px 6px 10px rgba(0,0,0,.12)}
.hero-wraps{left:630px;top:275px;width:210px;height:195px;border-radius:18px;background:radial-gradient(circle at 38% 30%,#f1ead6 0,#d9c9a8 12%,var(--biscuit) 17%,#e9e9e6 23%,transparent 40%),radial-gradient(circle at 68% 62%,#f1ead6 0,#d9c9a8 12%,var(--biscuit) 17%,#e9e9e6 23%,transparent 40%),linear-gradient(160deg,#f7f7f5,#e6e6e2)}

/* categories */
.cat-panel{left:96px;top:522px;width:260px;height:410px;background:linear-gradient(90deg,var(--cream) 80%,#e9e5da)}
.cat-head{left:96px;top:522px;width:260px;height:45px;background:linear-gradient(#8fb14a,#6d9128);color:#fff;font-size:20px;display:flex;align-items:center;justify-content:flex-end;padding-right:34px}
.cat-list{left:96px;top:592px;width:222px;list-style:none;text-align:right}
.cat-list li{height:42px;font-size:16.5px;color:var(--brown)}
.cat-list li::after{content:" »";margin-left:4px}
.cat-list li.is-current{color:var(--navy-text)}

/* products */
.section-title{left:378px;top:545px;font-size:21px;color:var(--brown)}
.round-arrow{width:19px;height:19px;border-radius:50%;background:#8d8a83}
.card{width:318px;height:137px;border:1px solid #dedbd3;background:linear-gradient(#fff,#f6f5f2)}
.card-art{position:absolute;left:15px;top:16px;width:150px;height:104px;border-radius:6px;background:radial-gradient(circle at 50% 50%,var(--tone) 0,var(--tone) 26%,var(--biscuit) 27%,var(--biscuit) 36%,#eceae6 38%,#f8f8f6 70%)}
.card-name{position:absolute;left:184px;top:16px;font-size:16.5px;color:var(--green)}
.card-desc{position:absolute;left:184px;top:44px;width:130px;font-size:13px;line-height:19px;color:var(--grey-text)}
.card-buy{position:absolute;left:186px;top:90px;font-size:18px;color:var(--buy);display:flex;align-items:center;gap:9px}

/* footer */
.site-footer{left:0;top:936px;width:1150px;height:244px;background:var(--footer)}
.testi-title{left:0;top:952px;width:1150px;text-align:center;font-size:21px;color:var(--lime)}
.testi-quote{left:0;top:994px;width:1150px;text-align:center;font-size:20px;color:#fff}
.testi-quote small{font-size:14px;color:var(--gold);font-weight:500}
.testi-copy{left:0;top:1027px;width:1150px;text-align:center;font-size:13px;color:var(--footer-text)}
.dark-arrow{width:26px;height:26px;border-radius:50%;background:#1b1b1b;border:1px solid #444}
.footer-rule{left:96px;top:1071px;width:959px;height:1px;background:#777}
.footer-nav{left:96px;top:1100px;font-size:13px;color:var(--footer-text)}
.footer-nav span{margin:0 9px;color:#999}
.copyright{left:96px;top:1135px;font-size:13px;color:var(--footer-text)}
.social{width:30px;height:30px;top:1111px;background:#cfcfcf;border-radius:2px}
</style>
</head>
<body>
<div class="page">

  <header class="site-header abs"></header>
  <nav class="main-nav">
    <a class="is-current" href="#" style="left:98px;top:15px">HOME</a>
    <a href="#" style="left:98px;top:41px">ABOUT US</a>
    <a href="#" style="left:98px;top:67px">SERVICES</a>
    <a href="#" style="left:228px;top:15px">SEND US A SIGN</a>
    <a href="#" style="left:228px;top:41px">ORDER NOW</a>
    <a href="#" style="left:228px;top:67px">CONTACT US</a>
  </nav>

  <div class="cart-title abs">My Cart</div>
  <svg class="cart-icon abs" width="38" height="34" viewBox="0 0 38 34" aria-hidden="true">
    <path d="M1 3h6l5 19h19l4-14H10" fill="none" stroke="#fff" stroke-width="3" stroke-linejoin="round"/>
    <circle cx="14" cy="29" r="3" fill="#fff"/><circle cx="28" cy="29" r="3" fill="#fff"/>
  </svg>
  <div class="cart-divider abs"></div>
  <div class="cart-info abs">
    (0) items in your cart<br>Total - $ 00.00<br>
    <span class="links">My Account<span>|</span>My List</span>
  </div>

  <section class="hero abs"></section>
  <h1 class="hero-title abs">Welcome to Zibbles</h1>
  <p class="hero-sub abs">Be miserable, or motivate yourself, it’s your choice!</p>
  <p class="hero-copy abs">A long time ago in a country far far away a very clever person invented the fortune cookie. Many many years later a couple of wise but demotivated women in New Zealand were munching some plain old cookies &amp; reading motivational quotes for fun.</p>
  <a class="btn-more abs" href="#">Read more</a>
  <div class="slider-dots abs"><i></i><i></i><i></i><i></i></div>
  <div class="hero-box abs" role="img" aria-label="Illustrated box of 14 chocolate chip biscuits"></div>
  <div class="hero-wraps abs" role="img" aria-label="Two individually wrapped chocolate chip biscuits with labels"></div>

  <div class="brand abs"><span class="brand-name">Zibbles</span><span class="brand-dot"></span></div>

  <aside class="cat-panel abs"></aside>
  <h2 class="cat-head abs">Zibbles Categories</h2>
  <ul class="cat-list abs">
    <li>Motivational Cookies</li>
    <li class="is-current">Adult Cookies</li>
    <li>Kids Cookies</li>
    <li>Christmas&nbsp; Cookies</li>
    <li>Animal Cookies</li>
    <li>Monster Cookies</li>
    <li>Cookies Box</li>
  </ul>

  <h2 class="section-title abs">Adult Cookies</h2>
  <div class="round-arrow abs" style="left:1014px;top:549px"></div>

  <article class="card abs" style="left:375px;top:596px">
    <div class="card-art" style="--tone:#a6c98a" role="img" aria-label="Wrapped biscuit with green quote label"></div>
    <h3 class="card-name">Aliquam sodales</h3>
    <p class="card-desc">Praesent varius enim ut vehicula varius.</p>
    <a class="card-buy" href="#"><svg width="18" height="16" viewBox="0 0 18 16" aria-hidden="true"><path d="M1 1h3l2 9h9l2-7H5" fill="none" stroke="currentColor" stroke-width="2"/><circle cx="7" cy="14" r="1.6" fill="currentColor"/><circle cx="14" cy="14" r="1.6" fill="currentColor"/></svg>BUY NOW</a>
  </article>
  <article class="card abs" style="left:716px;top:596px">
    <div class="card-art" style="--tone:#e5964f" role="img" aria-label="Wrapped biscuit with orange quote label"></div>
    <h3 class="card-name">Aliquam sodales</h3>
    <p class="card-desc">Praesent varius enim ut vehicula varius.</p>
    <a class="card-buy" href="#"><svg width="18" height="16" viewBox="0 0 18 16" aria-hidden="true"><path d="M1 1h3l2 9h9l2-7H5" fill="none" stroke="currentColor" stroke-width="2"/><circle cx="7" cy="14" r="1.6" fill="currentColor"/><circle cx="14" cy="14" r="1.6" fill="currentColor"/></svg>BUY NOW</a>
  </article>
  <article class="card abs" style="left:375px;top:757px">
    <div class="card-art" style="--tone:#ec7563" role="img" aria-label="Wrapped biscuit with red quote label"></div>
    <h3 class="card-name">Aliquam sodales</h3>
    <p class="card-desc">Praesent varius enim ut vehicula varius.</p>
    <a class="card-buy" href="#"><svg width="18" height="16" viewBox="0 0 18 16" aria-hidden="true"><path d="M1 1h3l2 9h9l2-7H5" fill="none" stroke="currentColor" stroke-width="2"/><circle cx="7" cy="14" r="1.6" fill="currentColor"/><circle cx="14" cy="14" r="1.6" fill="currentColor"/></svg>BUY NOW</a>
  </article>
  <article class="card abs" style="left:716px;top:757px">
    <div class="card-art" style="--tone:#7fb2d8" role="img" aria-label="Wrapped biscuit with blue quote label"></div>
    <h3 class="card-name">Aliquam sodales</h3>
    <p class="card-desc">Praesent varius enim ut vehicula varius.</p>
    <a class="card-buy" href="#"><svg width="18" height="16" viewBox="0 0 18 16" aria-hidden="true"><path d="M1 1h3l2 9h9l2-7H5" fill="none" stroke="currentColor" stroke-width="2"/><circle cx="7" cy="14" r="1.6" fill="currentColor"/><circle cx="14" cy="14" r="1.6" fill="currentColor"/></svg>BUY NOW</a>
  </article>

  <footer class="site-footer abs"></footer>
  <div class="dark-arrow abs" style="left:96px;top:950px"></div>
  <div class="dark-arrow abs" style="left:1027px;top:950px"></div>
  <h2 class="testi-title abs">Testimonials</h2>
  <p class="testi-quote abs">“A balanced diet is a Zibble in each hand” Marta <small>– Age 36 – Chicago</small></p>
  <p class="testi-copy abs">Since discovering Zibbles I have found the motivation to get out of bed each morning and have lost 25kg in 3 weeks by fuelling my mind and getting busy.</p>
  <div class="footer-rule abs"></div>
  <nav class="footer-nav abs">Home<span>|</span>About us<span>|</span>Services<span>|</span>Send us a Sign<span>|</span>Order Now<span>|</span>Contact us</nav>
  <p class="copyright abs">Copyright &nbsp;©&nbsp; 2013 &nbsp;Zibble Cookies. &nbsp;All rights reserved.</p>
  <div class="social abs" style="left:884px"></div>
  <div class="social abs" style="left:931px"></div>
  <div class="social abs" style="left:977px"></div>
  <div class="social abs" style="left:1024px"></div>

</div>
</body>
</html>
```